I need a new business card design for my pharmacy.

I need a business card design. I will include my logo.
The card needs to be readable. I prefer to have my logo on one side along with my website, the other side includes the other information. Please use combination of black, neon green, white, and silver. This needs to catch the eye but yet be clearly visible and legible. Thanks

Industry/Entity Type

Pharmacy

Contact Information for Business Card

It needs to have the following information listed:
Mel's Apothecary Owner/Pharm D.
7134 North Brook Lane
Sioux Falls, SD 57231
Phone 605-318-6207
Fax 605-318-6209
email: mel@melsapothecary-example.com
www.melsapothecary-example.com
Store hours Monday-Friday 8 am- 7 pm
Saturday 8 am- 12 pm
Sunday Closed
Please utilize the colors black, white, and neon green, maybe silver.

Requirements
Must have
• It needs to be easily readable!
Nice to have
• It should catch the eye.
Should not have
• Do not use any other colors except listed: black, neon green, white, & silver.

```html
<!DOCTYPE html>
<html lang="en">
<head>
<meta charset="utf-8">
<title>Mel's Apothecary Business Card</title>
<link href="https://fonts.googleapis.com/css2?family=Open+Sans:wght@400;600;700&display=swap" rel="stylesheet">
<style>
  :root {
    --backdrop: #3a3532;
    --card: #151515;
    --neon: #8cc63f;
    --white: #ffffff;
    --silver: #c9c9c9;
    --rule: #9a9a9a;
  }
  * { margin: 0; padding: 0; box-sizing: border-box; }
  html, body { width: 1200px; height: 814px; overflow: hidden; }
  body {
    background: var(--backdrop);
    font-family: "Open Sans", Arial, sans-serif;
    position: relative;
  }
  .card {
    position: absolute;
    top: 257px;
    width: 525px;
    height: 300px;
    background: var(--card);
    color: var(--white);
    box-shadow: 0 10px 30px rgba(0,0,0,.45);
  }
  .card--hours { left: 52px; }
  .card--contact { left: 623px; }

  /* Hours side */
  .hours-brand {
    position: absolute; top: 58px; left: 0; right: 0;
    text-align: center;
    font-size: 30px; font-weight: 600; color: var(--silver);
  }
  .hours-block {
    position: absolute; top: 128px; left: 50px; right: 50px;
    border-top: 1px solid var(--rule);
    border-bottom: 1px solid var(--rule);
    padding: 12px 0 14px;
    text-align: center;
  }
  .hours-title { color: var(--neon); font-weight: 700; font-size: 17px; letter-spacing: .5px; }
  .hours-week { font-size: 13px; margin-top: 4px; }
  .hours-closed { color: var(--neon); font-size: 17px; margin-top: 4px; }

  /* Contact side */
  .brand {
    position: absolute; top: 42px; right: 36px;
    display: flex; align-items: center; gap: 10px;
    font-size: 22px; font-weight: 700; color: var(--white);
  }
  .brand-dot { width: 14px; height: 14px; border-radius: 50%; background: var(--neon); }
  .person {
    position: absolute; top: 96px; left: 30px;
    border-left: 6px solid var(--neon);
    padding-left: 12px;
  }
  .person-title { color: var(--neon); font-size: 17px; font-weight: 600; line-height: 1.2; }
  .person-role { font-size: 14px; line-height: 1.2; }
  .divider {
    position: absolute; top: 132px; left: 98px; right: 30px;
    height: 1px; background: var(--rule);
  }
  .contact-list {
    position: absolute; top: 142px; left: 34px;
    list-style: none; font-size: 13px; line-height: 22px;
  }
  .contact-list li { display: flex; align-items: center; gap: 8px; }
  .contact-list svg { width: 13px; height: 13px; fill: var(--neon); flex: none; }
  .address {
    position: absolute; right: 32px; bottom: 14px;
    text-align: right; font-size: 14px; line-height: 21px;
    border-top: 1px solid var(--rule); padding-top: 8px; width: 240px;
  }
</style>
</head>
<body>
  <section class="card card--hours">
    <div class="hours-brand">Mel's Apothecary</div>
    <div class="hours-block">
      <div class="hours-title">STORE HOURS</div>
      <div class="hours-week">Monday to Friday : 8 am - 7 pm / Saturday : 8 am - 12 pm</div>
      <div class="hours-closed">Sunday Closed</div>
    </div>
  </section>

  <section class="card card--contact">
    <div class="brand"><span class="brand-dot"></span>Mel's Apothecary</div>
    <div class="person">
      <div class="person-title">Pharm D.</div>
      <div class="person-role">Owner</div>
    </div>
    <div class="divider"></div>
    <ul class="contact-list">
      <li><svg viewBox="0 0 16 16"><path d="M3 1l3 0 1.5 4-2 1.5a9 9 0 0 0 4 4L11 8.5l4 1.5 0 3a2 2 0 0 1-2 2A12 12 0 0 1 1 3a2 2 0 0 1 2-2z"/></svg>605-318-6207</li>
      <li><svg viewBox="0 0 16 16"><path d="M4 1h7v4H4z M1 6h14v7h-3v2H4v-2H1z M5 10v4h6v-4z"/></svg>605-318-6209</li>
      <li><svg viewBox="0 0 16 16"><path d="M1 3h14v10H1z"/><path d="M2 4l6 5 6-5" fill="none" stroke="#151515" stroke-width="1.4"/></svg>mel@melsapothecary-example.com</li>
    </ul>
    <div class="address">
      7134 North Brook Lane<br>
      Sioux Falls, SD 57231<br>
      www.melsapothecary-example.com
    </div>
  </section>
</body>
</html>
```